Real Estate - Large Sign Design

I am looking for a fresh new look for our leasing signs that will be showcase in front of commercial buildings available for lease. The sign dimension can be either 8'x4' or 4'x8'. They must exemplify our brand (see attachments) and be very visible by people driving by at high speeds.
They must include the following:
- Our logo (vector attached)
- Office Space Available
- 555-018-3274
- Nell Ruby
- Carl Ivey
- www.vantorile.com
Please let me know if you have any questions.
Target Market(s)
Drivers in high traffic areas, walking crowds
Industry/Entity Type
Real Estate
Requirements
Must have
- They must include the following:
- - Our logo (vector attached)
- - Office Space Available
- - 555-018-3274
- - Nell Ruby
- - Carl Ivey
- - www.vantorile.com
Should not have
- Should not be busy or hard to read.

```html
<!DOCTYPE html>
<html lang="en">
<head>
<meta charset="utf-8">
<title>Harrowgate Realty Group – Office Space Available</title>
<link href="https://fonts.googleapis.com/css2?family=Lato:wght@300;400;700&family=Montserrat:wght@700;800&family=Raleway:wght@200&display=swap" rel="stylesheet">
<style>
  :root {
    --panel-black: #000000;
    --white: #ffffff;
    --brand-green: #6cb359;
    --green-deep: #0e7a3a;
    --green-mid: #35a34a;
    --green-lime: #8cc63f;
    --slate-dark: #2b3a36;
    --slate-mid: #3f4f4a;
  }
  * { margin: 0; padding: 0; box-sizing: border-box; }
  html, body { width: 1200px; height: 600px; overflow: hidden; background: var(--white); }
  .sign { position: relative; width: 1200px; height: 600px; overflow: hidden; }
  .sign__backdrop { position: absolute; inset: 0; }
  .contact-panel {
    position: absolute; left: 52px; top: 0; width: 478px; height: 558px;
    background: var(--panel-black); color: var(--white);
    font-family: "Lato", sans-serif; text-align: center;
  }
  .brand-name {
    position: absolute; left: 0; right: 0; top: 52px;
    font-weight: 400; font-size: 46px; line-height: 52px; letter-spacing: 1px;
    text-transform: uppercase;
  }
  .contact-panel__rule {
    position: absolute; left: 78px; top: 250px; width: 323px; height: 1.5px;
    background: var(--brand-green);
  }
  .call-label { position: absolute; left: 0; right: 0; top: 280px; font-weight: 300; font-size: 33px; }
  .phone { position: absolute; left: 0; right: 0; top: 326px; font-weight: 700; font-size: 48px; color: var(--brand-green); letter-spacing: 0.5px; }
  .agents { position: absolute; left: 0; right: 0; top: 394px; font-weight: 300; font-size: 29px; line-height: 38px; text-transform: uppercase; list-style: none; }
  .website { position: absolute; left: 0; right: 0; top: 494px; font-weight: 400; font-size: 18px; letter-spacing: 0.3px; text-transform: uppercase; }
  .headline { position: absolute; inset: 0; }
</style>
</head>
<body>
<main class="sign">
  <svg class="sign__backdrop" width="1200" height="600" viewBox="0 0 1200 600" role="img" aria-label="City skyline and highway at dusk under a green tint">
    <defs>
      <linearGradient id="greenWash" x1="0" y1="0" x2="1" y2="1">
        <stop offset="0" stop-color="var(--green-deep)"/>
        <stop offset="0.55" stop-color="var(--green-mid)"/>
        <stop offset="1" stop-color="var(--green-lime)"/>
      </linearGradient>
      <linearGradient id="slateWash" x1="0" y1="0" x2="1" y2="1">
        <stop offset="0" stop-color="var(--slate-dark)"/>
        <stop offset="1" stop-color="#1f6a3c"/>
      </linearGradient>
    </defs>
    <rect width="1200" height="600" fill="url(#greenWash)"/>
    <polygon points="530,0 1200,0 1200,560 530,205" fill="url(#slateWash)" opacity="0.9"/>
    <polygon points="1055,0 1200,0 1200,600 930,600 1200,560 1200,230" fill="var(--slate-mid)" opacity="0.55"/>
  </svg>

  <section class="contact-panel">
    <p class="brand-name">Harrowgate<br>Realty<br>Group</p>
    <div class="contact-panel__rule"></div>
    <p class="call-label">CALL</p>
    <p class="phone">555-018-3274</p>
    <ul class="agents">
      <li>Nell Ruby</li>
      <li>Carl Ivey</li>
    </ul>
    <p class="website">www.vantorile.com</p>
  </section>

  <svg class="headline" width="1200" height="600" viewBox="0 0 1200 600" aria-label="Office Space Available">
    <g fill="var(--white)">
      <text x="598" y="228" font-family="Montserrat, sans-serif" font-weight="800" font-size="150" textLength="278" lengthAdjust="spacingAndGlyphs">OFF</text>
      <g class="building-icon">
        <rect x="890" y="120" width="42" height="108" rx="2"/>
        <g fill="var(--slate-dark)">
          <rect x="895" y="127" width="9" height="9"/><rect x="907" y="127" width="9" height="9"/><rect x="919" y="127" width="9" height="9"/>
          <rect x="895" y="140" width="9" height="9"/><rect x="907" y="140" width="9" height="9"/><rect x="919" y="140" width="9" height="9"/>
          <rect x="895" y="153" width="9" height="9"/><rect x="907" y="153" width="9" height="9"/><rect x="919" y="153" width="9" height="9"/>
          <rect x="895" y="166" width="9" height="9"/><rect x="907" y="166" width="9" height="9"/><rect x="919" y="166" width="9" height="9"/>
          <rect x="895" y="179" width="9" height="9"/><rect x="907" y="179" width="9" height="9"/><rect x="919" y="179" width="9" height="9"/>
          <rect x="905" y="206" width="12" height="22"/>
        </g>
      </g>
      <text x="944" y="228" font-family="Montserrat, sans-serif" font-weight="800" font-size="150" textLength="172" lengthAdjust="spacingAndGlyphs">CE</text>
      <text x="624" y="382" font-family="Raleway, sans-serif" font-weight="200" font-size="180" textLength="492" lengthAdjust="spacingAndGlyphs">SPACE</text>
      <text x="604" y="468" font-family="Montserrat, sans-serif" font-weight="700" font-size="94" textLength="516" lengthAdjust="spacingAndGlyphs">AVAILABLE</text>
    </g>
  </svg>
</main>
</body>
</html>
```